Barefoot Bowls A5 Flyer

We require an A5 Flyer to promote Barefoot Bowls at Wattlebrook Bowling Club. We want to promote Barefoot Bowls as a fun activity for all ages, and various occasions. (Private Functions including Birthdays, Christmas, Bucks and Hens Parties, as well as Corporate Functions, and Fundraising / Charity groups). The design should be bright and colourful, and include images of coloured Barefoot Bowls, as well as a Jumping Castle (which we offer as an optional extra). Price is $10 per person for 2 hours, and includes Instructor and Equipment. Various Catering options available. For Bookings or Enquiries call Peter on 0462 731 558, or Donna at the Club on 4391 2657. Club address is: 18-22 Hadley Street, Elderton NSW 2519.
Club

```html
<!DOCTYPE html>
<html lang="en">
<head>
<meta charset="utf-8">
<title>Barefoot Bowls – Wattlebrook Bowling Club</title>
<link href="https://fonts.googleapis.com/css2?family=Montserrat:wght@600&family=Oswald:wght@400;500&family=Quicksand:wght@500;600&family=Open+Sans:wght@700&display=swap" rel="stylesheet">
<style>
  :root {
    --grass: #4f8a2b;
    --grass-light: #6fa53a;
    --forest: #14301a;
    --lime: #8cc63f;
    --lime-fold: #5e9a2c;
    --band-dark: #1b6a34;
    --yellow: #e8e21c;
    --white: #ffffff;
    --ink-green: #13391c;
    --plum: #8e1f5f;
    --castle-fill: #e6e9f2;
  }
  * { margin: 0; padding: 0; box-sizing: border-box; }
  html, body { width: 914px; height: 1200px; overflow: hidden; background: #f2f2f2; }
  .flyer {
    position: relative; width: 914px; height: 1200px; overflow: hidden;
    background: var(--forest);
    font-family: "Quicksand", sans-serif;
  }
  .shapes { position: absolute; inset: 0; }
  .grass-photo {
    position: absolute; left: 0; top: 0; width: 914px; height: 720px;
    background:
      radial-gradient(ellipse at 70% 35%, var(--grass-light) 0%, transparent 60%),
      linear-gradient(180deg, #5d9632 0%, var(--grass) 45%, #2d5a1f 78%, var(--forest) 100%);
  }
  .headline {
    position: absolute; left: 50px; top: 200px;
    transform: rotate(-7deg); transform-origin: left top;
    font-family: "Montserrat", sans-serif; font-weight: 600;
    color: var(--yellow); line-height: 0.92; letter-spacing: 2px;
  }
  .headline-small { display: block; font-size: 84px; }
  .headline-large { display: block; font-size: 146px; margin-left: 52px; }
  .club-line {
    position: absolute; left: 40px; top: 492px;
    transform: rotate(-7deg); transform-origin: left top;
    font-family: "Oswald", sans-serif; font-weight: 500;
    font-size: 72px; color: var(--white); white-space: nowrap; line-height: 1;
  }
  .ribbon-text {
    position: absolute; left: 166px; top: 612px;
    transform: rotate(-6deg); transform-origin: left top;
    font-family: "Oswald", sans-serif; font-weight: 400;
    font-size: 52px; line-height: 1; color: var(--white); letter-spacing: 2px; white-space: nowrap;
  }
  .details { position: absolute; left: 32px; top: 712px; color: var(--white); }
  .details-title { font-size: 26px; font-weight: 500; letter-spacing: 1.5px; margin-bottom: 16px; line-height: 30px; }
  .details-text { font-size: 23px; font-weight: 500; line-height: 30px; letter-spacing: 1.2px; white-space: nowrap; }
  .price { margin-top: 42px; color: var(--yellow); font-size: 22px; line-height: 31px; letter-spacing: 1px; }
  .catering { margin-top: 28px; color: var(--yellow); font-size: 22px; letter-spacing: 1px; }
  .castle-badge { position: absolute; left: 658px; top: 818px; width: 210px; height: 210px; }
  .castle-label {
    position: absolute; left: 700px; top: 946px; width: 124px; text-align: center;
    font-family: "Quicksand", sans-serif; font-weight: 600; color: var(--white);
    font-size: 18px; line-height: 21px; letter-spacing: 0.5px;
  }
  .contact {
    position: absolute; left: 0; top: 1050px; width: 914px; text-align: center;
    font-family: "Oswald", sans-serif; font-weight: 500; color: var(--ink-green);
  }
  .contact-lead { font-size: 28px; line-height: 38px; }
  .contact-call { font-size: 30px; line-height: 40px; }
  .contact-address {
    margin-top: 4px; display: flex; justify-content: center; align-items: center; gap: 8px;
    font-family: "Open Sans", sans-serif; font-weight: 700; font-size: 21px; color: var(--white);
  }
</style>
</head>
<body>
<main class="flyer">
  <div class="grass-photo" role="img" aria-label="Photo of bare feet standing on a lawn bowling green with coloured bowls and a white jack"></div>

  <svg class="shapes" width="914" height="1200" viewBox="0 0 914 1200" aria-hidden="true">
    <polygon points="60,660 900,566 890,620 50,724 20,702" fill="#0d2411" opacity="0.5"/>
    <polygon points="22,618 84,610 74,672 8,680 40,650" fill="var(--lime-fold)"/>
    <polygon points="60,605 878,520 892,598 72,690" fill="var(--lime)"/>
    <polygon points="852,524 914,516 900,548 914,584 864,590" fill="var(--lime-fold)"/>
    <polygon points="0,1062 914,1030 914,1200 0,1200" fill="var(--lime)"/>
    <polygon points="0,1168 914,1186 914,1200 0,1200" fill="var(--band-dark)"/>
    <g transform="translate(763,923)">
      <circle r="88" fill="var(--white)"/>
      <circle r="90" fill="none" stroke="var(--white)" stroke-width="14" stroke-linecap="round" stroke-dasharray="0 11.3"/>
    </g>
  </svg>

  <h1 class="headline">
    <span class="headline-small">BAREFOOT</span>
    <span class="headline-large">BOWLS</span>
  </h1>
  <p class="club-line">at Wattlebrook Bowling Club</p>
  <p class="ribbon-text">FUN ACTIVITY FOR ALL AGES</p>

  <section class="details">
    <h2 class="details-title">VARIOUS OCCASIONS</h2>
    <p class="details-text">Private Functions including Birthdays, Christmas, Bucks<br>and Hens Parties, as well as Corporate Functions, and<br>Fundraising / Charity groups</p>
    <p class="price">$10 PER PERSON FOR 2 HOURS,<br>and includes Instructor and Equipment</p>
    <p class="catering">Various Catering options available</p>
  </section>

  <svg class="castle-badge" viewBox="0 0 210 210">
    <defs><clipPath id="badge-clip"><circle cx="105" cy="105" r="78"/></clipPath></defs>
    <rect x="40" y="30" width="130" height="110" clip-path="url(#badge-clip)" fill="var(--castle-fill)" role="img" aria-label="Illustration of a colourful inflatable jumping castle"/>
    <path d="M26,122 L184,122 L180,158 Q105,196 30,158 Z" fill="var(--plum)"/>
  </svg>
  <p class="castle-label">JUMPING<br>CASTLE</p>

  <footer class="contact">
    <p class="contact-lead">For Bookings or Enquiries</p>
    <p class="contact-call">call Peter on 0462 731 558, or Donna at the Club on 4391 2657</p>
    <p class="contact-address">
      <svg width="14" height="20" viewBox="0 0 14 20" aria-hidden="true"><path d="M7,0 C3,0 0,3 0,7 C0,12 7,20 7,20 C7,20 14,12 14,7 C14,3 11,0 7,0 Z M7,10 A3,3 0 1 1 7,4 A3,3 0 1 1 7,10 Z" fill="var(--white)"/></svg>
      18-22 Hadley Street, Elderton NSW 2519
    </p>
  </footer>
</main>
</body>
</html>
```